Stationary and digital Media for Health & Wellness company
Vital Progress by Measured Research
Stationary and digital Media for Health & Wellness company - Health
Creative Brief
Use same font as used in my logo
or easy to read font
Modern
Marisol Quenby
Nutritional Practitioner
2836 Harlow Ln Crofton, MD 21114
(XXX) XXX-XXXX
Marisol@Vitalora-Wellpath.example
www.Vitalora-Wellpath.example
Would like to see both Color Logo on White background and on Black Background, or combination of complimentary colors. Twitter/FB/Instagram icons, possible QR code on front or back
Logo only or logo w/bullet list of services and QR code
belgrave52 belgrave52
Fantastic job on the revisions we ask for! We should be able to pick something out of what you’ve got. Hopefully we will finalize with in the next day or so
Can you use #133 and put a thin blue line on the right side of the leaf where it abuts the green on the front of the card. Thank you
Please change Website to www.Purevine-Thrive.example and use @Purevine-Thrive.example for email addresses

```html
<!DOCTYPE html>
<html lang="en">
<head>
<meta charset="utf-8">
<title>Purevine Thrive – Business Cards</title>
<link rel="stylesheet" href="https://fonts.googleapis.com/css2?family=Open+Sans:wght@400;600;700&display=swap">
<style>
:root{
  --backdrop:#3b3c3e;
  --card-white:#ffffff;
  --card-black:#050607;
  --brand-blue:#2a4fa3;
  --brand-blue-light:#4f79d6;
  --brand-green:#5aa832;
  --leaf-green:#7cc243;
  --text-grey:#555a60;
  --text-dark:#2d3136;
  --text-light:#e8ebef;
  --photo-top:#d7d9dc;
  --photo-bottom:#9a9ea4;
}
*{box-sizing:border-box;margin:0;padding:0}
html,body{width:1200px;height:751px;overflow:hidden}
body{background:var(--backdrop);font-family:"Open Sans",Arial,sans-serif;position:relative}
.card{position:absolute;overflow:hidden;box-shadow:0 6px 18px rgba(0,0,0,.45)}
.card--front{left:350px;top:53px;width:461px;height:283px;background:var(--card-white)}
.card--back{top:389px;width:490px;height:288px}
.card--back-light{left:82px;background:var(--card-white)}
.card--back-dark{left:624px;background:var(--card-black)}

.portrait{position:absolute;left:82px;top:43px;width:70px;height:116px;
  background:linear-gradient(180deg,var(--photo-top),var(--photo-bottom));border:1px solid #c8cacd}
.person-name{position:absolute;left:82px;top:182px;font-size:15px;font-weight:600;color:var(--brand-blue);white-space:nowrap}
.person-role{position:absolute;left:82px;top:204px;font-size:8.5px;color:var(--text-grey);white-space:nowrap}

.brand{position:absolute;display:flex;flex-direction:column;align-items:center;width:190px}
.brand-mark{width:var(--mark,56px);height:var(--mark,56px);border-radius:50%;background:var(--leaf-green)}
.brand-name{margin-top:var(--gap,8px);font-weight:700;font-size:var(--brand-size,20px);line-height:1.2;color:var(--brand-blue);letter-spacing:.3px;white-space:nowrap}
.card--front .brand{left:270px;top:16px;--mark:56px;--brand-size:19px;--gap:30px}
.card--back .brand{left:51px;top:79px;--mark:62px;--brand-size:20px;--gap:12px}
.card--back-dark .brand-name{color:var(--brand-blue-light)}

.contact-list{position:absolute;left:262px;top:146px;list-style:none}
.contact-list li{display:flex;align-items:center;height:15px;font-size:8.5px;color:var(--text-grey);white-space:nowrap}
.contact-list svg{width:10px;height:10px;margin-right:6px;flex:none}

.swoosh{position:absolute;left:0;top:0}
.tagline{position:absolute;right:16px;bottom:11px;text-align:right;color:#fff;font-size:9.5px;font-weight:600;line-height:13px;white-space:nowrap}

.services{position:absolute;left:268px;top:62px}
.services-title{font-size:13px;font-weight:700;color:var(--brand-blue);margin-bottom:3px}
.card--back-dark .services-title{color:var(--brand-blue-light)}
.service-list{list-style:none}
.service-list li{display:flex;align-items:center;height:18.5px;font-size:10.5px;color:var(--text-dark);white-space:nowrap}
.card--back-dark .service-list li{color:var(--text-light)}
.service-list svg{width:10px;height:10px;margin-right:6px;flex:none}
.website{margin-top:4px;font-size:12px;font-weight:700;color:var(--brand-blue);white-space:nowrap}
.card--back-dark .website{color:var(--brand-blue-light)}

.social-row{position:absolute;left:86px;top:246px;display:flex;gap:20px}
.social-row span{display:flex;align-items:center;font-size:8.5px;color:var(--text-dark);white-space:nowrap}
.card--back-dark .social-row span{color:var(--text-light)}
.social-row i{display:inline-block;width:9px;height:9px;background:var(--brand-blue);margin-right:4px}
</style>
</head>
<body>

<section class="card card--front">
  <div class="portrait" role="img" aria-label="Portrait photo of the practitioner"></div>
  <div class="brand">
    <div class="brand-mark"></div>
    <div class="brand-name">Purevine Thrive</div>
  </div>
  <p class="person-name">Marisol Quenby</p>
  <p class="person-role">Nutritional Practitioner</p>
  <ul class="contact-list">
    <li><svg viewBox="0 0 10 10"><path d="M2 1h2l1 2-1.2 1a5 5 0 0 0 2.2 2.2L7 5l2 1v2a1 1 0 0 1-1 1A7 7 0 0 1 1 2a1 1 0 0 1 1-1z" fill="#2a4fa3"/></svg>(555) 014-2270</li>
    <li><svg viewBox="0 0 10 10"><rect x="2.5" y="0.5" width="5" height="9" rx="1" fill="#2a4fa3"/><rect x="3.5" y="1.8" width="3" height="5.5" fill="#fff"/></svg>(555) 014-8813</li>
    <li><svg viewBox="0 0 10 10"><rect x="0.5" y="2" width="9" height="6" fill="#2a4fa3"/><path d="M0.5 2l4.5 3.5L9.5 2" stroke="#fff" fill="none" stroke-width=".8"/></svg>Marisol@Purevine-Thrive.example</li>
    <li><svg viewBox="0 0 10 10"><circle cx="5" cy="5" r="4.3" fill="none" stroke="#2a4fa3" stroke-width="1"/><path d="M.7 5h8.6M5 .7c-2.4 2.6-2.4 6 0 8.6M5 .7c2.4 2.6 2.4 6 0 8.6" stroke="#2a4fa3" fill="none" stroke-width=".7"/></svg>www.Purevine-Thrive.example</li>
  </ul>
  <svg class="swoosh" width="461" height="283" viewBox="0 0 461 283">
    <path d="M0 238C130 226 300 222 461 220L461 227C300 230 140 238 0 250Z" fill="#5aa832"/>
    <path d="M0 283L0 262C150 244 300 234 461 230L461 283Z" fill="#2a4fa3"/>
  </svg>
  <p class="tagline">Advancing Vital Progress<br>by Measured Research</p>
</section>

<section class="card card--back card--back-light">
  <div class="brand">
    <div class="brand-mark"></div>
    <div class="brand-name">Purevine Thrive</div>
  </div>
  <div class="services">
    <p class="services-title">SERVICES</p>
    <ul class="service-list">
      <li><svg viewBox="0 0 10 10"><path d="M1 5l3 3 5-7" stroke="#5aa832" stroke-width="2" fill="none"/></svg>Muscle Response testing</li>
      <li><svg viewBox="0 0 10 10"><path d="M1 5l3 3 5-7" stroke="#5aa832" stroke-width="2" fill="none"/></svg>Organic Whole food supplement</li>
      <li><svg viewBox="0 0 10 10"><path d="M1 5l3 3 5-7" stroke="#5aa832" stroke-width="2" fill="none"/></svg>Heart rate Variability Scan</li>
      <li><svg viewBox="0 0 10 10"><path d="M1 5l3 3 5-7" stroke="#5aa832" stroke-width="2" fill="none"/></svg>Weight Loss</li>
      <li><svg viewBox="0 0 10 10"><path d="M1 5l3 3 5-7" stroke="#5aa832" stroke-width="2" fill="none"/></svg>Health Maintenance</li>
      <li><svg viewBox="0 0 10 10"><path d="M1 5l3 3 5-7" stroke="#5aa832" stroke-width="2" fill="none"/></svg>Non-Invasive</li>
    </ul>
    <p class="website">Purevine-Thrive.example</p>
  </div>
  <div class="social-row">
    <span><i></i>PurevineThrive1</span>
    <span><i></i>@PurevineThrive1</span>
    <span><i></i>PurevineThrive1</span>
  </div>
</section>

<section class="card card--back card--back-dark">
  <div class="brand">
    <div class="brand-mark"></div>
    <div class="brand-name">Purevine Thrive</div>
  </div>
  <div class="services">
    <p class="services-title">SERVICES</p>
    <ul class="service-list">
      <li><svg viewBox="0 0 10 10"><path d="M1 5l3 3 5-7" stroke="#5aa832" stroke-width="2" fill="none"/></svg>Muscle Response testing</li>
      <li><svg viewBox="0 0 10 10"><path d="M1 5l3 3 5-7" stroke="#5aa832" stroke-width="2" fill="none"/></svg>Organic Whole food supplement</li>
      <li><svg viewBox="0 0 10 10"><path d="M1 5l3 3 5-7" stroke="#5aa832" stroke-width="2" fill="none"/></svg>Heart rate Variability Scan</li>
      <li><svg viewBox="0 0 10 10"><path d="M1 5l3 3 5-7" stroke="#5aa832" stroke-width="2" fill="none"/></svg>Weight Loss</li>
      <li><svg viewBox="0 0 10 10"><path d="M1 5l3 3 5-7" stroke="#5aa832" stroke-width="2" fill="none"/></svg>Health Maintenance</li>
      <li><svg viewBox="0 0 10 10"><path d="M1 5l3 3 5-7" stroke="#5aa832" stroke-width="2" fill="none"/></svg>Non-Invasive</li>
    </ul>
    <p class="website">Purevine-Thrive.example</p>
  </div>
  <div class="social-row">
    <span><i></i>PurevineThrive1</span>
    <span><i></i>@PurevineThrive1</span>
    <span><i></i>PurevineThrive1</span>
  </div>
</section>

</body>
</html>
```